TG - management consultant

Business card - contemporary design

Front info
Thomas Galloway

(Address not necessary)
PO Box 7324
Ashford, CA 94071

(650) 482-3719
tg@thomasgallo.wy

Chirper: tgq287
FriendBook: /Thomas.Galloway
ProNet: /in/thomasgalloway

Back or Front
www.thomasgalloway.net
Facilitation & coaching, change management, strategic partnerships, business improvement

Target Market(s)

High tech businesses - mostly startups in Silicon Valley

Industry/Entity Type

Business

Font styles to use
Sans Serif

Colors

Designer to choose colors to be used in the design.

```html
<!DOCTYPE html>
<html lang="en">
<head>
<meta charset="utf-8">
<title>Thomas Galloway – Business Card</title>
<link rel="stylesheet" href="https://fonts.googleapis.com/css2?family=Arimo:wght@400&display=swap">
<style>
  :root {
    --blue: #2283c9;
    --grey: #58585a;
    --white: #ffffff;
    --soft-grey: #c9c9c9;
    --service: #d4d9de;
    --divider: #1e1e1e;
    --page: #ffffff;
  }
  * { box-sizing: border-box; margin: 0; padding: 0; }
  html, body {
    width: 1200px;
    height: 343px;
    overflow: hidden;
    background: var(--page);
  }
  .card {
    position: relative;
    width: 1200px;
    height: 343px;
    overflow: hidden;
    font-family: "Arimo", Arial, sans-serif;
    font-weight: 400;
    color: var(--white);
  }
  .card__shapes {
    position: absolute;
    inset: 0;
    width: 1200px;
    height: 343px;
  }
  .card__shapes .shape-grey { fill: var(--grey); }
  .card__shapes .shape-blue { fill: var(--blue); }
  .card__shapes .fold-line {
    stroke: var(--divider);
    stroke-width: 1.4;
    stroke-dasharray: 2 2;
  }
  .text {
    position: absolute;
    white-space: nowrap;
    line-height: 1;
    font-weight: 400;
    transform: translateY(-50%);
  }
  .name { left: 34px; top: 36px; font-size: 29px; color: var(--white); }
  .phone { right: 635px; top: 38px; font-size: 23px; color: var(--soft-grey); }
  .services { font-size: 22px; color: var(--service); left: 34px; }
  .services--1 { top: 105px; }
  .services--2 { top: 145px; }
  .services--3 { top: 184px; }
  .services--4 { top: 229px; }
  .address { left: 34px; font-size: 19px; color: var(--white); }
  .address--1 { top: 296px; }
  .address--2 { top: 322px; }
  .email { right: 637px; top: 312px; font-size: 23px; color: var(--white); }
  .website { left: 895px; top: 153px; font-size: 27px; color: var(--white); transform: translate(-50%, -50%); }
  .social {
    position: absolute;
    display: flex;
    align-items: center;
    gap: 10px;
    font-size: 15px;
    color: var(--white);
    white-space: nowrap;
    transform: translateY(-50%);
  }
  .social__mark {
    width: 26px;
    height: 26px;
    background: var(--blue);
    flex: none;
  }
  .social--chirper { left: 632px; top: 262px; }
  .social--pronet { left: 632px; top: 310px; }
  .social--friendbook { left: 918px; top: 310px; }
</style>
</head>
<body>
  <main class="card">
    <svg class="card__shapes" viewBox="0 0 1050 300" preserveAspectRatio="none" aria-hidden="true">
      <rect class="shape-grey" x="0" y="0" width="525" height="300"/>
      <path class="shape-blue" d="M0,58 C230,48 430,110 525,290 L525,300 L0,300 Z"/>
      <rect class="shape-grey" x="525" y="0" width="525" height="300"/>
      <path class="shape-blue" d="M527,0 L1050,0 L1050,218 C880,212 680,205 600,140 C560,105 540,55 532,0 Z"/>
      <line class="fold-line" x1="525" y1="0" x2="525" y2="300"/>
    </svg>

    <section class="front">
      <h1 class="text name">Thomas Galloway</h1>
      <p class="text phone">(650) 482-3719</p>
      <p class="text services services--1">Change Management</p>
      <p class="text services services--2">Facilitation &amp; Coaching</p>
      <p class="text services services--3">Business Improvement</p>
      <p class="text services services--4">Strategic Partnerships</p>
      <p class="text address address--1">PO Box 7324</p>
      <p class="text address address--2">Ashford, CA 94071</p>
      <p class="text email">tg@thomasgallo.wy</p>
    </section>

    <section class="back">
      <p class="text website">www.thomasgalloway.net</p>
      <p class="social social--chirper"><span class="social__mark"></span>chirper.com/tgq287</p>
      <p class="social social--pronet"><span class="social__mark"></span>pronet.com/in/thomasgalloway</p>
      <p class="social social--friendbook"><span class="social__mark"></span>friendbook.com/Thomas.Galloway</p>
    </section>
  </main>
</body>
</html>
```